Agricultural Consulting Website

Provide a modern yet business like website for my new Agriculture Consulting Business in Australia called FenTrove. Whilst we are based in Australia we are targetting both domestic and international markets (especially in Asia). We are targetting corporate, small business, government and farmer clients. The design should compliment our logo also sourced through pixel guild. The webiste should be easy for me to keep updated on a regular basis without the need to go back to the designer.

Industry/Entity Type

Business

Requirements
Must have
• clean crisp feel
• be modern yet business like
• be able to be updated by myself easily

```html
<!DOCTYPE html>
<html lang="en">
<head>
<meta charset="utf-8">
<title>FenTrove – Agriculture Consulting</title>
<link rel="stylesheet" href="https://fonts.googleapis.com/css2?family=Open+Sans:wght@400;600&family=Roboto:wght@300;400;500&display=swap">
<style>
:root{
  --green:#5a9e12;
  --green-dark:#3f7a08;
  --green-light:#8cc63f;
  --brown:#6b3a1c;
  --caption:rgba(120,60,30,.82);
  --text:#555;
  --head:#222;
  --white:#fff;
  --field:#e6e6e6;
}
*{margin:0;padding:0;box-sizing:border-box}
html,body{width:900px;height:1200px;overflow:hidden}
body{position:relative;font-family:"Open Sans",sans-serif;color:var(--text);
  background:linear-gradient(90deg,#9a5a26 0%,#c99043 30%,#e7c27a 60%,#c68a3a 85%,#8f4f20 100%)}
.backdrop{position:absolute;inset:0;background:radial-gradient(ellipse at 50% 20%,rgba(255,235,180,.6),transparent 60%),linear-gradient(180deg,rgba(255,255,255,.15),rgba(120,60,20,.35))}
.page{position:absolute;left:66px;top:0;width:770px;height:1200px}
.header{position:absolute;left:0;top:0;width:770px;height:66px;background:var(--white)}
.brand{position:absolute;left:41px;top:28px;display:flex;align-items:center;gap:6px;font-family:"Roboto",sans-serif;font-size:18px;color:var(--green)}
.brand-mark{width:14px;height:14px;background:var(--green-dark)}
.phone{position:absolute;right:42px;top:16px;font:500 11px "Roboto",sans-serif;color:var(--brown);display:flex;align-items:center;gap:3px}
.social{position:absolute;right:42px;top:40px;display:flex;gap:5px}
.social span{width:14px;height:14px;border-radius:2px}
.nav{position:absolute;left:0;top:66px;width:770px;height:28px;background:linear-gradient(#7dbb2c,#4f9210);display:flex;align-items:center;padding-left:40px;gap:15px;font-size:10px;color:var(--white)}
.nav .current{color:#2e5a06}
.search{position:absolute;right:42px;top:4px;width:140px;height:18px;background:var(--white);border-radius:3px}
.search svg{position:absolute;right:2px;top:1px}
.hero{position:absolute;left:0;top:94px;width:770px;height:334px;background:linear-gradient(180deg,#6d5a5a 0%,#d98a3e 30%,#c27a40 50%,#8a5a3a 70%,#b0683a 100%)}
.cap{position:absolute;left:41px;background:var(--caption);color:var(--white);font-size:18px;padding:3px 7px}
.cap-text{position:absolute;left:41px;top:141px;width:298px;height:101px;background:rgba(230,205,195,.55);padding:7px;font-size:8.2px;line-height:15px;color:#222}
.btn-brown{display:inline-block;background:var(--brown);color:var(--white);font-size:7px;padding:2px 4px;border-radius:2px;margin-top:2px}
.content{position:absolute;left:0;top:428px;width:770px;height:542px;background:var(--white)}
.welcome h1{position:absolute;left:0;width:770px;top:18px;text-align:center;font:400 17px "Roboto",sans-serif;color:var(--head)}
.welcome h1 em{font-style:normal;color:var(--green)}
.welcome p{position:absolute;left:48px;width:674px;top:47px;text-align:center;font-size:8.3px;line-height:11px}
.more{position:absolute;top:90px;width:770px;text-align:center;font-size:8.5px;color:var(--green)}
.divider{position:absolute;top:118px;height:10px;width:330px;background:radial-gradient(ellipse at 50% 0%,rgba(0,0,0,.35),transparent 70%)}
.testi{position:absolute;left:17px;top:143px;width:735px;height:143px;border:1px solid #eee;border-radius:3px;box-shadow:0 0 4px rgba(0,0,0,.06)}
.testi h2{text-align:center;margin-top:8px;font:400 17px "Roboto",sans-serif;color:var(--head)}
.avatar{position:absolute;left:73px;top:42px;width:64px;height:64px;border-radius:50%;border:3px solid #2a1c12;background:linear-gradient(#c9a27a,#8a6a4a)}
.quote{position:absolute;left:151px;top:65px;width:520px;font-size:8.3px;line-height:13px}
.quote cite{display:block;font-size:7.5px;font-style:italic;color:#333}
.arrow{position:absolute;top:60px}
.service{position:absolute;top:310px;width:230px}
.service .icon{position:absolute;left:0;top:0;width:56px;height:56px;border-radius:50%;border:1px solid #333;background:#fff}
.service .icon i{position:absolute;inset:10px;border-radius:50%;background:#6a6a6a}
.service h3{position:absolute;left:61px;top:2px;font:400 17px "Roboto",sans-serif;color:var(--head);white-space:nowrap}
.service p{position:absolute;left:62px;top:25px;width:155px;font-size:8px;line-height:8.5px}
.btn-green{position:absolute;top:73px;background:linear-gradient(#6cb31f,#3f7f08);color:var(--white);font-size:7px;padding:3px 4px;border-radius:2px;border:1px solid #cfe8b0}
.news h2{position:absolute;top:436px;width:770px;text-align:center;font:400 17px "Roboto",sans-serif;color:var(--head)}
.news .rule{position:absolute;left:280px;top:456px;width:208px;height:1px;background:#ccc}
.news .rule:before,.news .rule:after{content:"";position:absolute;top:-3px;width:7px;height:7px;border-radius:50%;background:#ccc}
.news .rule:before{left:-3px}.news .rule:after{right:-3px}
.item{position:absolute;top:472px}
.item .thumb{position:absolute;left:0;top:0;width:47px;height:48px}
.item p{position:absolute;left:54px;top:-4px;width:135px;font-size:8.3px;line-height:13.5px}
.item b{position:absolute;left:170px;top:36px;color:var(--green);font-size:10px}
.footer{position:absolute;left:0;top:970px;width:770px;height:230px;background:linear-gradient(180deg,rgba(150,100,30,.55),rgba(190,120,40,.45));color:var(--white)}
.footer h4{position:absolute;top:18px;font:400 17px "Roboto",sans-serif}
.fline{position:absolute;top:44px;height:1px;background:var(--green-light)}
.fline:after{content:"";position:absolute;right:-2px;top:-2px;width:5px;height:5px;border-radius:50%;background:var(--green-light)}
.flinks{position:absolute;left:42px;top:56px;list-style:none;font-size:8.5px;line-height:17.6px}
.flinks li:first-child{color:#c7f06a}
.ftext{position:absolute;left:275px;top:56px;width:215px;font-size:8.3px;line-height:13.5px}
.email{position:absolute;left:276px;top:124px;width:181px;height:24px;background:var(--field);color:#333;font-size:7.5px;padding:8px 7px}
.join{position:absolute;left:457px;top:124px;width:32px;height:24px;background:linear-gradient(#6cb31f,#3f7f08);font-size:9px;text-align:center;line-height:24px}
.privacy{position:absolute;left:277px;top:154px;font-size:8.3px}
.field{position:absolute;left:540px;width:188px;background:var(--field);color:#333;font-size:9px;text-align:center;border:1px solid #ddd}
.submit{position:absolute;left:586px;top:174px;width:70px;height:24px;background:linear-gradient(#6cb31f,#3f7f08);font-size:9.5px;text-align:center;line-height:24px}
.copy{position:absolute;top:206px;width:770px;text-align:center;font-size:8.3px}
</style>
</head>
<body>
<div class="backdrop" role="img" aria-label="Blurred autumn field with bare trees in warm orange light"></div>
<div class="page">
  <header class="header">
    <div class="brand"><span class="brand-mark"></span>FenTrove</div>
    <div class="phone"><svg width="8" height="10" viewBox="0 0 8 10"><path d="M2 0 L4 2 L3 4 Q4 6 6 7 L8 6 L8 9 Q3 10 0 3 Q0 1 2 0Z" fill="#3f7a08"/></svg>1-800-555-0142</div>
    <div class="social"><span style="background:#c8232c"></span><span style="background:#3b5998"></span><span style="background:#3a9ad9"></span><span style="background:#555"></span></div>
  </header>
  <nav class="nav">
    <span class="current">Home</span><span>About</span><span>Activities</span><span>Events</span><span>Members</span><span>Positions Vacant</span><span>Contact Us</span>
    <div class="search"><svg width="22" height="16" viewBox="0 0 22 16"><rect width="22" height="16" rx="2" fill="#4f9210"/><circle cx="10" cy="7" r="4" fill="none" stroke="#fff" stroke-width="1.5"/><line x1="13" y1="10" x2="16" y2="13" stroke="#fff" stroke-width="1.5"/></svg></div>
  </nav>
  <section class="hero" role="img" aria-label="Sunset over a dry paddock with bare trees and wooden fence posts">
    <div class="cap" style="top:74px">Lorem ipsum dolor sit amet</div>
    <div class="cap" style="top:108px;width:234px">Consectetur adipisicing</div>
    <div class="cap-text">Lorem ipsum dolor sit amet, consectetur adipisicing elit, sed do eiusmod tempor incididunt ut labore et dolore magna aliqua. Ut enim ad minim veniam, quis nostrud exercitation ullamco laboris nisi ut aliquip<br><span class="btn-brown">Read more</span></div>
  </section>
  <main class="content">
    <div class="welcome">
      <h1>Welcome to <em>FenTrove</em></h1>
      <p>Lorem ipsum dolor sit amet, consectetur adipisicing elit, sed do eiusmod tempor incididunt ut labore et dolore magna aliqua. Ut enim ad minim veniam, quis nostrud exercitation ullamco laboris nisi ut aliquip ex ea commodo consequat. Duis aute irure dolor in reprehenderit in voluptate velit esse cillum dolore eu fugiat nulla pariatur. Excepteur sint occaecat cupidatat non proident, sunt in culpa qui officia deserunt mollit anim id est laborum</p>
      <div class="more">Read more &raquo;</div>
      <div class="divider" style="left:45px"></div><div class="divider" style="left:410px"></div>
    </div>
    <section class="testi">
      <h2>Testimonials</h2>
      <svg class="arrow" style="left:10px" width="12" height="20" viewBox="0 0 12 20"><polyline points="10,2 2,10 10,18" fill="none" stroke="#333" stroke-width="1.3"/></svg>
      <svg class="arrow" style="right:10px" width="12" height="20" viewBox="0 0 12 20"><polyline points="2,2 10,10 2,18" fill="none" stroke="#8cc63f" stroke-width="1.3"/></svg>
      <div class="avatar" role="img" aria-label="Portrait of a client"></div>
      <div class="quote">Lorem ipsum dolor sit amet, consectetur adipisicing elit, sed do eiusmod tempor incididunt ut labore et dolore magna aliqua. laboris nisi ut aliquip &nbsp;consequat. Duis aut irure dolor in reprehenderit in voluptate velit esse cillum dolore eu fugiat nulla pariatur.<cite>Daniel Hart</cite></div>
    </section>
    <section class="service" style="left:41px"><div class="icon" role="img" aria-label="Wheat emblem"><i></i></div><h3>Agriculture Consulting</h3><p>Lorem ipsum dolor sit amet, consectetur adipisicing elit, sed do eiusmod tempor incididunt ut labore et dolore magna aliqua.</p><span class="btn-green" style="left:63px">Read more</span></section>
    <section class="service" style="left:288px"><div class="icon" role="img" aria-label="Seeds"><i></i></div><h3 style="left:65px">Seed</h3><p style="left:66px">Lorem ipsum dolor sit amet, consectetur adipisicing elit, sed do eiusmod tempor incididunt ut labore et dolore magna aliqua.</p><span class="btn-green" style="left:65px">Read more</span></section>
    <section class="service" style="left:517px"><div class="icon" role="img" aria-label="Forklift"><i></i></div><h3>Service</h3><p>Lorem ipsum dolor sit amet, consectetur adipisicing elit, sed do eiusmod tempor incididunt ut labore et dolore magna aliqua.</p><span class="btn-green" style="left:63px">Read more</span></section>
    <section class="news">
      <h2>Agriculture news</h2><div class="rule"></div>
      <div class="item" style="left:43px"><div class="thumb" role="img" aria-label="Green crop rows under blue sky" style="background:linear-gradient(#7fb2e0 35%,#3f8a20 36%,#2d6a12)"></div><p>Lorem ipsum dolor sit amet, eiusmod tempor incididunt ut ad minim veniam, quis nostrud aliquip ex ea commodo</p><b>&raquo;</b></div>
      <div class="item" style="left:296px"><div class="thumb" role="img" aria-label="Harvester in golden wheat" style="background:linear-gradient(#a8c4d8 30%,#c8963c 31%,#a2702a)"></div><p>Lorem ipsum dolor sit amet eiusmod tempor incididunt ut ad minim veniam, quis nostrud aliquip ex ea commodo</p><b>&raquo;</b></div>
      <div class="item" style="left:549px"><div class="thumb" role="img" aria-label="Tree beside a yellow field" style="background:linear-gradient(#c9d6dd 30%,#4a6a2a 31%,#5a7a2a 65%,#d8c040 66%)"></div><p>Lorem ipsum dolor sit amet eiusmod tempor incididunt ut ad minim veniam, quis nostrud aliquip ex ea commodo</p><b>&raquo;</b></div>
    </section>
  </main>
  <footer class="footer">
    <h4 style="left:41px">Navigation</h4><div class="fline" style="left:41px;width:161px"></div>
    <ul class="flinks"><li>Home</li><li>About</li><li>Activities</li><li>Events</li><li>Members</li><li>Positions Vacant</li><li>Contact Us</li></ul>
    <h4 style="left:274px">Newsletter Sign up</h4><div class="fline" style="left:274px;width:214px"></div>
    <p class="ftext">Lorem ipsum dolor sit amet, consectetur adipisicing elit, sed do eiusmod tempor incididunt ut labore et dolore magna aliqua. Ut enim ad minim veniam, quis nostrud exercitation ullamco laboris nisi ut aliquip ex</p>
    <div class="email">Email address</div><div class="join">Join</div>
    <div class="privacy">We respect your privacy</div>
    <h4 style="left:539px">Feedback</h4><div class="fline" style="left:539px;width:188px"></div>
    <div class="field" style="top:60px;height:24px;line-height:22px">Name</div>
    <div class="field" style="top:88px;height:24px;line-height:22px">E-mail</div>
    <div class="field" style="top:116px;height:52px;padding-top:3px">Message</div>
    <div class="submit">Submit</div>
    <div class="copy">&copy; 2013, Copy Right for FenTrove. All rights reserved</div>
  </footer>
</div>
</body>
</html>
```